Lone Plains Civic Builders Summit Needs a Flyer

One-page event graphic/flyer and header needed. Logos provided.

2023 Lone Plains Civic Builders Summit
Steady Footing – Fresh Tales, Fresh Fixes, Fresh Wins
August 10-11, 2023
San Antonio, Texas

About the Forum:
“Capital projects are full of risk. It’s not a question of eliminating risk, it’s a question of how to clearly identify it, reduce it, change it, or battle it.”
- Miriam Dobrantova, Founder, Q-ArkVT; San Antonio City Architect (retired)

Fresh Tales, Fresh Fixes, Fresh Wins: Q-ArkVT’s Lone Plains Civic Builders Summit (LPCBS) is designed to help you attain project success by hearing from Public Project Owners, architects, engineers, consultants, contractors, and suppliers. We are all in this together, and Q-ArkVT is the organization that champions cross-collaboration and communication for project success!

For reference in design ONLY -
Here are some topic areas that bring project risks and/or rewards and that ultimately affect the Public Project Owner’s project success:

• Project Planning
• Regional Growth Shifts
• Project Funding
• Contracting
• Governmental Regulations
• Long-term COVID Impacts
• Infrastructure and Site Design
• Safety and Security
• Sustainability and Resilience
• Construction Predictability
• Leveraging Technology
• Facility Operations

Target Market(s)

Architects, Engineers, Contractors, project owners

Industry/Entity Type

Design and Construction

Requirements
Must have
• This is for a one-page (8.5x11) event graphic/flyer only - logos are provided. Q-ArkVT logo, Lone Plains Civic Builders Summit (LPCBS) logo, 2023 Lone Plains Civic Builders Summit, date, location
Nice to have
• Graphic(s) that represent the design and construction industry and the theme of this event (title, topics covered)
Should not have
• Full project description

```html
<!DOCTYPE html>
<html lang="en">
<head>
<meta charset="utf-8">
<title>Lone Plains Civic Builders Summit – Flyer and Header</title>
<link rel="stylesheet" href="https://fonts.googleapis.com/css2?family=Poppins:wght@300;400;600;700;800&display=swap">
<style>
:root{
  --board:#080d22;
  --blue:#1f4ea3;
  --blue-band:#1c3f8f;
  --green:#8cb43a;
  --green-band:#5f7d24;
  --grey:#5b5b5b;
  --sky-top:#f4fbff;
  --sky-low:#a9dcf2;
  --label:#3d8bb1;
  --white:#ffffff;
}
*{margin:0;padding:0;box-sizing:border-box}
html,body{width:853px;height:1200px;overflow:hidden;background:var(--board);font-family:"Poppins",sans-serif}
.board{position:relative;width:853px;height:1200px}
.piece{position:absolute;background:var(--white);overflow:hidden}
.abs{position:absolute}
.scene{background:linear-gradient(180deg,var(--sky-top) 0%,#d6f0fb 45%,var(--sky-low) 100%)}
.skyline{background:linear-gradient(180deg,rgba(150,185,210,0) 0%,rgba(130,165,190,.45) 55%,rgba(105,140,170,.7) 100%)}
.figure{background:linear-gradient(180deg,rgba(95,125,165,0) 0%,rgba(80,115,165,.55) 22%,rgba(70,105,155,.75) 60%,rgba(55,75,105,.85) 100%);border-radius:90px 90px 0 0}
.title{font-weight:800;text-transform:uppercase;line-height:1;letter-spacing:-.5px}
.title .g{color:var(--green)} .title .b{color:var(--blue)}
.band-blue{background:var(--blue-band)}
.band-green{background:var(--green-band)}
.event-name{color:var(--blue);font-weight:600;text-align:right;line-height:1.15}
.tagline{font-weight:800;line-height:.95;text-transform:uppercase}
.checks{list-style:none}
.checks li{display:flex;align-items:center;gap:4px}
.checks svg{flex:none}
.org{display:flex;align-items:center;gap:8px}
.org-dot{border-radius:50%;background:var(--blue)}
.org-name{color:var(--grey);font-weight:400}
.contact{color:var(--grey)}
.contact .sep{color:var(--blue);margin:0 6px}
.label{position:absolute;color:var(--label);font-weight:300;letter-spacing:6px;transform:rotate(-90deg);transform-origin:left top;font-size:20px}
</style>
</head>
<body>
<div class="board">

  <!-- FLYER -->
  <section class="piece flyer" style="left:175px;top:85px;width:502px;height:650px">
    <div class="abs scene" style="left:0;top:0;width:502px;height:545px"></div>
    <div class="abs skyline" style="left:0;top:330px;width:502px;height:215px" role="img" aria-label="Photo: city skyline sketch being drawn by a hand with a marker, tower cranes behind"></div>
    <div class="abs figure" style="left:268px;top:160px;width:234px;height:385px" role="img" aria-label="Photo: construction professional in a blue shirt holding an orange hard hat and rolled plans"></div>

    <div class="abs" style="left:41px;top:38px;font-size:38px;font-weight:300;color:var(--grey);line-height:1">2023</div>
    <h1 class="abs title" style="left:41px;top:84px;font-size:40px;line-height:45px">
      <span class="g">Lone Plains</span><br><span class="g">Civic</span><br><span class="b">Builders</span><br><span class="b">Summit</span>
    </h1>
    <div class="abs event-name" style="left:320px;top:52px;width:140px;font-size:17px">Lone Plains<br>Civic Builders<br>Summit</div>

    <div class="abs band-blue" style="left:0;top:458px;width:502px;height:45px"></div>
    <div class="abs band-green" style="left:0;top:503px;width:502px;height:42px"></div>
    <div class="abs" style="left:41px;top:465px;color:var(--white);font-size:26px;line-height:1"><b style="font-weight:700">August 10-11,</b> 2023</div>
    <div class="abs" style="left:41px;top:506px;color:var(--white);font-size:28px;font-weight:700;line-height:1">San Antonio, Texas</div>

    <div class="abs tagline" style="left:41px;top:574px;font-size:25px">
      <span style="color:var(--blue)">Steady</span><br><span style="color:var(--green)">Footing</span>
    </div>
    <ul class="abs checks" style="left:180px;top:572px;font-size:13px;line-height:16px">
      <li><svg width="11" height="11" viewBox="0 0 12 12"><circle cx="6" cy="6" r="5" fill="none" stroke="var(--green)" stroke-width="1.2"/><path d="M3.5 6.2l1.8 1.7 3.2-3.4" fill="none" stroke="var(--green)" stroke-width="1.2"/></svg><span style="color:var(--green)">Fresh <b style="color:var(--blue);font-weight:600">Tales</b></span></li>
      <li><svg width="11" height="11" viewBox="0 0 12 12"><circle cx="6" cy="6" r="5" fill="none" stroke="var(--green)" stroke-width="1.2"/><path d="M3.5 6.2l1.8 1.7 3.2-3.4" fill="none" stroke="var(--green)" stroke-width="1.2"/></svg><span style="color:var(--green)">Fresh <b style="color:var(--blue);font-weight:600">Fixes</b></span></li>
      <li><svg width="11" height="11" viewBox="0 0 12 12"><circle cx="6" cy="6" r="5" fill="none" stroke="var(--green)" stroke-width="1.2"/><path d="M3.5 6.2l1.8 1.7 3.2-3.4" fill="none" stroke="var(--green)" stroke-width="1.2"/></svg><span style="color:var(--green)">Fresh <b style="color:var(--blue);font-weight:600">Wins</b></span></li>
    </ul>
    <div class="abs org" style="left:336px;top:560px">
      <span class="org-dot" style="width:36px;height:36px"></span>
      <span class="org-name" style="font-size:22px">Q-ArkVT</span>
    </div>
    <div class="abs contact" style="left:330px;top:612px;font-size:8px">(555) 014-7720<span class="sep">|</span>www.q-arkvt.org</div>
  </section>
  <div class="label" style="left:141px;top:734px">FLYER</div>

  <!-- HEADER -->
  <section class="piece header" style="left:128px;top:810px;width:597px;height:298px">
    <div class="abs scene" style="left:0;top:0;width:597px;height:298px"></div>
    <div class="abs skyline" style="left:330px;top:100px;width:267px;height:95px" role="img" aria-label="Photo: tower cranes and sketched skyline with a drawing hand"></div>
    <div class="abs figure" style="left:225px;top:70px;width:125px;height:228px;border-radius:60px 60px 0 0" role="img" aria-label="Photo: construction professional holding an orange hard hat and rolled plans"></div>

    <div class="abs" style="left:36px;top:92px;font-size:30px;font-weight:300;color:var(--grey);line-height:1;transform:rotate(-90deg);transform-origin:left top">2023</div>
    <h2 class="abs title" style="left:71px;top:18px;font-size:32px;line-height:37px">
      <span class="g">Lone Plains</span><br><span class="g">Civic</span>
    </h2>
    <h2 class="abs title" style="left:36px;top:96px;font-size:34px;line-height:38px">
      <span class="b">Builders</span><br><span class="b">Summit</span>
    </h2>

    <div class="abs" style="left:299px;top:19px;width:22px;height:53px;background:var(--green)"></div>
    <div class="abs" style="left:302px;top:69px;font-size:15px;font-weight:600;color:var(--white);line-height:1;transform:rotate(-90deg);transform-origin:left top">2023</div>
    <div class="abs" style="left:326px;top:18px;color:var(--blue);font-size:27px;font-weight:700;line-height:26px">AUG<br>10-11</div>
    <div class="abs event-name" style="left:440px;top:22px;width:130px;font-size:14px">Lone Plains<br>Civic Builders<br>Summit</div>

    <div class="abs" style="left:0;top:206px;width:232px;height:92px;background:var(--white)"></div>
    <div class="abs org" style="left:47px;top:222px">
      <span class="org-dot" style="width:38px;height:38px"></span>
      <span class="org-name" style="font-size:22px">Q-ArkVT</span>
    </div>
    <div class="abs contact" style="left:44px;top:272px;font-size:9px">(555) 014-7720<span class="sep">|</span>www.q-arkvt.org</div>

    <div class="abs band-blue" style="left:345px;top:195px;width:252px;height:40px"></div>
    <div class="abs band-green" style="left:345px;top:235px;width:252px;height:63px"></div>
    <div class="abs" style="left:367px;top:203px;color:var(--white);font-size:19px;font-weight:700;line-height:1">San Antonio, Texas</div>
    <div class="abs tagline" style="left:368px;top:245px;font-size:18px;color:var(--white)">Steady<br>Footing</div>
    <ul class="abs checks" style="left:482px;top:242px;font-size:10px;line-height:13px;color:var(--white);font-weight:600">
      <li><svg width="9" height="9" viewBox="0 0 12 12"><circle cx="6" cy="6" r="5" fill="none" stroke="#fff" stroke-width="1.3"/><path d="M3.5 6.2l1.8 1.7 3.2-3.4" fill="none" stroke="#fff" stroke-width="1.3"/></svg>Fresh Tales</li>
      <li><svg width="9" height="9" viewBox="0 0 12 12"><circle cx="6" cy="6" r="5" fill="none" stroke="#fff" stroke-width="1.3"/><path d="M3.5 6.2l1.8 1.7 3.2-3.4" fill="none" stroke="#fff" stroke-width="1.3"/></svg>Fresh Fixes</li>
      <li><svg width="9" height="9" viewBox="0 0 12 12"><circle cx="6" cy="6" r="5" fill="none" stroke="#fff" stroke-width="1.3"/><path d="M3.5 6.2l1.8 1.7 3.2-3.4" fill="none" stroke="#fff" stroke-width="1.3"/></svg>Fresh Wins</li>
    </ul>
  </section>
  <div class="label" style="left:744px;top:1110px">HEADER</div>

</div>
</body>
</html>
```